Banner Ad Design

We require a banner ad design for 4 Brands.

Banner 1: Willowmere on the Brook
Please follow url http://www.seniorhavenresidences.example/index.php/willowmere-on-the-brook/welcome for art, logo, tagline.

Banner 2: Noble Trellis
Please follow url http://www.seniorhavenresidences.example/index.php/noble-trellis/welcome for art, logo, tagline.

Banner 3: Trellis Meadows
Please follow url http://www.seniorhavenresidences.example/index.php/trellis-meadows/welcome for art, logo, tagline.

Banner 4: Marbury Court
http://www.seniorhavenresidences.example/index.php/marbury-court/welcome

ALL Banners consists of - 1. LOGO, 2. TAGLINE: Experience and uncompromising Retirement Lifestyle. 3. CALL TO ACTION: View Images, Download the Brochure, Register for More.

Each brand must be broken into the following Sizes:

468 × 60
728 × 90
250 × 250
200 × 200
336 × 280
300 × 250
120 × 600
160 × 600
300 × 600
970 × 90
240 × 400
980 × 120
930 × 180
250 × 360
580 × 400
150kb max size

Target Market(s)

Seniors and their middle age children

Industry/Entity Type

Royal

Requirements
Must have
• 468 × 60
728 × 90
250 × 250
200 × 200
336 × 280
300 × 250
120 × 600
160 × 600
300 × 600
970 × 90
240 × 400
980 × 120
930 × 180
250 × 360
580 × 400
150kb max size
Nice to have
• large font for easy viewing - images of the experience
Should not have
• any pictures of decrepit people, or dying people - must be fun and vibrant.

```html
<!DOCTYPE html>
<html lang="en">
<head>
<meta charset="utf-8">
<title>Trellis Meadows – Banner Set</title>
<link href="https://fonts.googleapis.com/css2?family=Antonio:wght@400;600&display=swap" rel="stylesheet">
<style>
:root{
  --board:#3a1d12;
  --white:#ffffff;
  --brand-ink:#2d2466;
  --green-light:#7aa536;
  --green-mid:#4f7a1f;
  --green-dark:#1f3a0c;
  --orange:#f7941d;
  --orange-light:#ffc23a;
  --orange-deep:#e57a0c;
  --cream:#ffffff;
  --btn-ink:#3b1c00;
}
*{margin:0;padding:0;box-sizing:border-box}
html,body{width:1200px;height:837px;overflow:hidden}
body{background:var(--board);position:relative;font-family:"Antonio",sans-serif}
.banner{position:absolute;overflow:hidden;background:var(--green-dark)}
.banner svg.art{position:absolute;inset:0;width:100%;height:100%}
.logo-box{position:absolute;background:var(--white);display:flex;align-items:center;gap:8px;padding-left:12px}
.logo-mark{width:30px;height:30px;border-radius:50%;background:var(--green-mid);flex:none}
.logo-name{color:var(--brand-ink);font-weight:400;text-transform:uppercase;line-height:1.05;font-size:20px;letter-spacing:.5px}
.tagline{position:absolute;text-transform:uppercase;font-weight:400;white-space:nowrap}
.tagline .soft{display:block;color:var(--cream)}
.tagline .bold{display:block;color:var(--orange);font-weight:600}
.cta{position:absolute;display:flex;align-items:center;justify-content:center;gap:8px;
  background:linear-gradient(var(--orange-light),var(--orange) 55%,var(--orange-deep));
  border:1px solid #ffd98a;border-radius:4px;color:var(--btn-ink);text-transform:uppercase;
  font-size:15px;box-shadow:0 1px 3px rgba(0,0,0,.45);white-space:nowrap}
.cta svg{width:16px;height:16px;flex:none}

/* 160 x 600 skyscraper */
.sky{left:43px;top:52px;width:199px;height:755px}
.sky .logo-box{left:0;top:0;width:199px;height:100px}
.sky .tagline{left:0;right:0;top:478px;text-align:center}
.sky .soft{font-size:25px;line-height:31px}
.sky .bold{font-size:36px;line-height:39px}
.sky .cta{left:10px;top:703px;width:180px;height:32px}

/* 728 x 90 leaderboard */
.leader{left:255px;top:52px;width:916px;height:111px}
.leader .logo-box{left:0;top:0;width:182px;height:111px;align-items:flex-start;padding-top:10px}
.leader .logo-name{font-size:18px}
.leader .logo-mark{width:26px;height:26px}
.leader .tagline{left:400px;right:20px;top:16px;text-align:center}
.leader .soft{font-size:31px;line-height:38px}
.leader .bold{font-size:33px;line-height:38px}
.leader .cta{left:7px;top:70px;width:168px;height:33px}

/* 336 x 280 rectangle */
.rect-lg{left:255px;top:187px;width:423px;height:352px}
.rect-lg .logo-box{left:0;top:0;width:193px;height:73px}
.rect-lg .tagline{left:7px;top:102px}
.rect-lg .soft{font-size:27px;line-height:32px}
.rect-lg .bold{font-size:40px;line-height:42px}
.rect-lg .cta{left:65px;top:309px;width:178px;height:32px}

/* 300 x 250 rectangle */
.rect-md{left:688px;top:225px;width:379px;height:314px}
.rect-md .logo-box{left:0;top:0;width:170px;height:78px}
.rect-md .logo-name{font-size:18px}
.rect-md .tagline{left:6px;top:90px}
.rect-md .soft{font-size:25px;line-height:29px}
.rect-md .bold{font-size:36px;line-height:38px}
.rect-md .cta{left:59px;top:275px;width:159px;height:30px;font-size:13px}
</style>
</head>
<body>

<svg width="0" height="0" style="position:absolute">
  <defs>
    <linearGradient id="greenFade" x1="0" y1="0" x2="0" y2="1">
      <stop offset="0" stop-color="#7aa536"/>
      <stop offset=".55" stop-color="#4f7a1f"/>
      <stop offset="1" stop-color="#1f3a0c"/>
    </linearGradient>
    <linearGradient id="greenSide" x1="0" y1="0" x2="1" y2="0">
      <stop offset="0" stop-color="#2a4a10"/>
      <stop offset=".5" stop-color="#4f7a1f"/>
      <stop offset="1" stop-color="#2a4a10"/>
    </linearGradient>
    <linearGradient id="photoTone" x1="0" y1="0" x2="1" y2="1">
      <stop offset="0" stop-color="#8a7a4a"/>
      <stop offset=".45" stop-color="#b9a88c"/>
      <stop offset="1" stop-color="#3d5a8a"/>
    </linearGradient>
  </defs>
</svg>

<!-- 160 x 600 -->
<section class="banner sky">
  <svg class="art" viewBox="0 0 199 755" preserveAspectRatio="none">
    <rect x="0" y="100" width="199" height="360" fill="url(#photoTone)" role="img" aria-label="Photo of a smiling senior woman with her adult daughter outdoors"/>
    <path d="M0,445 Q45,525 199,408 L199,755 L0,755 Z" fill="url(#greenFade)"/>
    <path d="M0,445 Q45,525 199,408" fill="none" stroke="var(--orange)" stroke-width="4"/>
  </svg>
  <div class="logo-box"><span class="logo-mark"></span><span class="logo-name">Trellis<br>Meadows</span></div>
  <p class="tagline"><span class="soft">Experience an</span><span class="soft">Uncompromising</span><span class="bold">&amp; Affordable</span><span class="bold">Retirement</span><span class="bold">Lifestyle</span></p>
  <a class="cta">Register for more<svg viewBox="0 0 16 16"><circle cx="8" cy="8" r="8" fill="#111"/><path d="M6.5 4.5 10 8l-3.5 3.5" fill="none" stroke="#fff" stroke-width="2"/></svg></a>
</section>

<!-- 728 x 90 -->
<section class="banner leader">
  <svg class="art" viewBox="0 0 916 111" preserveAspectRatio="none">
    <rect x="0" y="0" width="916" height="111" fill="url(#greenSide)"/>
    <rect x="182" y="0" width="7" height="111" fill="#1f3a0c"/>
    <path d="M189,0 L385,0 Q360,60 395,111 L189,111 Z" fill="url(#photoTone)" role="img" aria-label="Photo of a senior woman and her adult daughter smiling together"/>
    <path d="M385,0 Q360,60 395,111" fill="none" stroke="var(--orange)" stroke-width="4"/>
  </svg>
  <div class="logo-box"><span class="logo-mark"></span><span class="logo-name">Trellis<br>Meadows</span></div>
  <p class="tagline"><span class="soft">Experience an uncompromising</span><span class="bold">&amp; Affordable retirement lifestyle</span></p>
  <a class="cta">Register for more<svg viewBox="0 0 16 16"><circle cx="8" cy="8" r="8" fill="#111"/><path d="M6.5 4.5 10 8l-3.5 3.5" fill="none" stroke="#fff" stroke-width="2"/></svg></a>
</section>

<!-- 336 x 280 -->
<section class="banner rect-lg">
  <svg class="art" viewBox="0 0 423 352" preserveAspectRatio="none">
    <rect x="0" y="0" width="423" height="352" fill="url(#greenFade)"/>
    <path d="M193,0 L423,0 L423,352 L318,352 C255,260 210,130 193,0 Z" fill="url(#photoTone)" role="img" aria-label="Photo of a smiling adult daughter embracing her senior mother outdoors"/>
    <path d="M193,0 C210,130 255,260 318,352" fill="none" stroke="var(--orange)" stroke-width="4"/>
  </svg>
  <div class="logo-box"><span class="logo-mark"></span><span class="logo-name">Trellis<br>Meadows</span></div>
  <p class="tagline"><span class="soft">Experience an</span><span class="soft">Uncompromising</span><span class="bold">&amp; Affordable</span><span class="bold">Retirement</span><span class="bold">Lifestyle</span></p>
  <a class="cta">Register for more<svg viewBox="0 0 16 16"><circle cx="8" cy="8" r="8" fill="#111"/><path d="M6.5 4.5 10 8l-3.5 3.5" fill="none" stroke="#fff" stroke-width="2"/></svg></a>
</section>

<!-- 300 x 250 -->
<section class="banner rect-md">
  <svg class="art" viewBox="0 0 379 314" preserveAspectRatio="none">
    <rect x="0" y="0" width="379" height="314" fill="url(#greenFade)"/>
    <path d="M170,0 L379,0 L379,314 L284,314 C228,232 186,116 170,0 Z" fill="url(#photoTone)" role="img" aria-label="Photo of a smiling adult daughter embracing her senior mother outdoors"/>
    <path d="M170,0 C186,116 228,232 284,314" fill="none" stroke="var(--orange)" stroke-width="4"/>
  </svg>
  <div class="logo-box"><span class="logo-mark"></span><span class="logo-name">Trellis<br>Meadows</span></div>
  <p class="tagline"><span class="soft">Experience an</span><span class="soft">Uncompromising</span><span class="bold">&amp; Affordable</span><span class="bold">Retirement</span><span class="bold">Lifestyle</span></p>
  <a class="cta">Register for more<svg viewBox="0 0 16 16"><circle cx="8" cy="8" r="8" fill="#111"/><path d="M6.5 4.5 10 8l-3.5 3.5" fill="none" stroke="#fff" stroke-width="2"/></svg></a>
</section>

</body>
</html>
```